Father's Day Email Blast Graphic

Need a classic Father's Day email blast newsletter graphic - smiling dad with son, upscale casual. Text to read: FREE shipping on ALL orders!, Make it special for Dad, monogram it!, 40%-75% off store wide sale (some exclusions apply) for www.corvantel.com.

Industry/Entity Type

Shipping

```html
<!DOCTYPE html>
<html lang="en">
<head>
<meta charset="utf-8">
<title>Corvantel Father's Day Mailer</title>
<link rel="stylesheet" href="https://fonts.googleapis.com/css2?family=Oswald:wght@700&family=Roboto+Slab:wght@800;900&family=Open+Sans:wght@400;600&display=swap">
<style>
  :root {
    --navy: #1d3a63;
    --red: #e2311d;
    --orange: #e8482a;
    --sky-top: #4fb3e6;
    --sky-bottom: #cdeefb;
    --grass: #7cc243;
    --grass-dark: #4f9a2a;
    --white: #ffffff;
    --frame: #9a9a9a;
    --ink: #2b2b2b;
    --figure-a: #8aa8c0;
    --figure-b: #e0a27a;
  }
  * { margin: 0; padding: 0; box-sizing: border-box; }
  html, body { width: 900px; height: 1200px; overflow: hidden; background: var(--white); }
  .mailer {
    position: relative; width: 900px; height: 1200px; overflow: hidden;
    border: 3px solid var(--frame);
    background: linear-gradient(180deg, var(--sky-top) 0%, var(--sky-bottom) 80%);
  }
  .masthead {
    position: absolute; left: 0; top: 0; width: 100%; height: 168px;
    background: var(--white);
    display: flex; flex-direction: column; align-items: center; justify-content: center; gap: 8px;
  }
  .brand {
    display: flex; align-items: center; gap: 14px;
    font-family: "Oswald", sans-serif; font-weight: 700; font-size: 54px;
    color: var(--ink); letter-spacing: 1px; line-height: 1;
  }
  .brand-mark { width: 34px; height: 34px; background: var(--ink); }
  .tagline {
    font-family: "Open Sans", sans-serif; font-weight: 600; font-size: 15px;
    color: var(--ink); letter-spacing: 1.5px;
  }
  .headline {
    position: absolute; left: 62px; top: 190px;
    font-family: "Oswald", sans-serif; font-weight: 700; font-size: 108px;
    line-height: 1.02; color: var(--navy); text-transform: uppercase;
  }
  .headline .accent { color: var(--orange); }
  .shipping {
    position: absolute; left: 64px; top: 530px;
    font-family: "Roboto Slab", serif; font-weight: 800; font-size: 44px;
    color: var(--red);
  }
  .grass {
    position: absolute; left: 0; bottom: 0; width: 100%; height: 190px;
    background: linear-gradient(180deg, var(--grass) 0%, var(--grass-dark) 100%);
  }
  .figures {
    position: absolute; left: 180px; top: 610px; width: 480px; height: 540px;
    border-radius: 120px 120px 20px 20px;
    background: linear-gradient(180deg, var(--figure-b) 0%, var(--figure-a) 45%, #3a4a5c 100%);
    opacity: 0.85;
  }
  .briefcase {
    position: absolute; left: 110px; top: 1030px; width: 120px; height: 85px;
    border-radius: 10px; background: #222;
  }
  .sale-sign {
    position: absolute; left: 590px; top: 800px; width: 220px; height: 270px;
    background: var(--white); border: 2px solid #ccc;
    display: flex; flex-direction: column; align-items: center; justify-content: center;
    font-family: "Roboto Slab", serif; font-weight: 900; color: var(--red);
    text-align: center; line-height: 1;
  }
  .sale-range { font-size: 42px; }
  .sale-off { font-size: 72px; }
  .sale-store { font-size: 34px; font-weight: 800; margin-top: 4px; }
  .sale-word { font-size: 64px; }
  .exclusions {
    position: absolute; right: 36px; bottom: 26px;
    font-family: "Open Sans", sans-serif; font-weight: 600; font-size: 16px; color: var(--white);
  }
</style>
</head>
<body>
<main class="mailer">
  <header class="masthead">
    <div class="brand"><span class="brand-mark"></span>CORVANTEL.COM</div>
    <p class="tagline">BRIEFCASES &amp; BAGS FOR TRAVEL SINCE 1998</p>
  </header>

  <h1 class="headline">Make it special<br>for <span class="accent">Dad</span>,<br>monogram it!</h1>
  <p class="shipping">FREE shipping on ALL orders!</p>

  <div class="grass"></div>
  <div class="figures" role="img" aria-label="Illustration of a smiling father in a sweater and his son holding a sale sign"></div>
  <div class="briefcase" role="img" aria-label="Illustration of a black leather briefcase on the grass"></div>

  <div class="sale-sign">
    <span class="sale-range">40%-75%</span>
    <span class="sale-off">OFF</span>
    <span class="sale-store">store wide</span>
    <span class="sale-word">SALE</span>
  </div>

  <p class="exclusions">(some exclusions apply)</p>
</main>
</body>
</html>
```